Business Card

Company: Willow Ridge Nursery.

Use uploaded logo or design one just like it. This is a tree growing operation and really like earth tone colors.

Target Market(s)

Landscaping company's, retail nurseries, and landscape arc.

Industry/Entity Type

Business

Font styles to use
Serif

Requirements
Must have
• Name: Dale Whitford
Title: Owner
Address: 48217 W. 150 Road, Grove, OK 74592
Office: 918-555-3172
Cell: 918-555-6094
Fax: 918-555-4418
email: dalewr@plainsmail.net
Willow Ridge Nursery

```html
<!DOCTYPE html>
<html lang="en">
<head>
<meta charset="utf-8">
<title>Willow Ridge Nursery – Business Cards</title>
<link href="https://fonts.googleapis.com/css2?family=Lato:wght@400;700&display=swap" rel="stylesheet">
<style>
  :root {
    --backdrop: #8f8f8f;
    --card: #f9f9f9;
    --green: #33865b;
    --green-light: #74b792;
    --text: #3a3a3a;
    --art-fill: #e3efe7;
  }
  * { margin: 0; padding: 0; box-sizing: border-box; }
  html, body { width: 1200px; height: 750px; overflow: hidden; }
  body {
    position: relative;
    background: var(--backdrop);
    font-family: "Lato", Arial, sans-serif;
    color: var(--text);
  }
  .showcase-title {
    position: absolute;
    top: 112px; left: 0; width: 1200px;
    text-align: center;
    font-size: 44px;
    font-weight: 400;
    color: var(--green);
    letter-spacing: 1px;
  }
  .card {
    position: absolute;
    top: 202px;
    width: 525px; height: 300px;
    border-radius: 18px;
    background: var(--card);
    overflow: hidden;
  }
  .card--front { left: 62px; }
  .card--back { left: 607px; }
  .green-panel {
    position: absolute; top: 0; height: 300px;
    background: linear-gradient(180deg, var(--green) 0%, var(--green) 18%, var(--green-light) 32%, var(--green) 55%, var(--green) 100%);
  }
  .card--front .green-panel { left: 340px; right: 0; }
  .card--back .green-panel { left: 0; width: 165px; }
  .tree-art {
    position: absolute; top: 0; width: 185px; height: 300px;
    background: var(--art-fill);
  }
  .card--front .tree-art { left: 283px; }
  .card--back .tree-art { left: 54px; }
  .company {
    position: absolute; top: 34px;
    font-size: 24px; font-weight: 400; color: var(--green);
  }
  .card--front .company { left: 24px; }
  .card--back .company { right: 24px; }
  .details {
    position: absolute; font-size: 13px; line-height: 15px;
  }
  .card--front .details { left: 24px; top: 113px; }
  .card--back .details { right: 24px; top: 104px; text-align: right; }
  .details__name { font-size: 16px; font-weight: 700; color: var(--green); line-height: 19px; }
  .card--front .details__role { margin-bottom: 8px; }
  .card--front .details__address { margin-bottom: 7px; }
  .card--back .details__role { margin-bottom: 14px; }
  .card--back .details__address { margin-bottom: 15px; }
  .contact-list { list-style: none; }
  .contact-list li { display: flex; align-items: center; gap: 8px; height: 15px; }
  .card--back .contact-list li { justify-content: flex-end; }
  .contact-icon { width: 13px; height: 12px; fill: var(--green); flex: none; }
</style>
</head>
<body>
  <h1 class="showcase-title">Willow Ridge Nursery</h1>

  <section class="card card--front">
    <div class="green-panel"></div>
    <div class="tree-art" role="img" aria-label="Company illustration: young tree with balled roots and a small shrub"></div>
    <p class="company">Willow Ridge Nursery</p>
    <div class="details">
      <p class="details__name">Dale Whitford</p>
      <p class="details__role">Owner</p>
      <p class="details__address">48217 W. 150 Road, Grove,<br>OK 74592</p>
      <ul class="contact-list">
        <li><svg class="contact-icon" viewBox="0 0 13 12"><path d="M1 4c0-2 2-3 5.5-3S12 2 12 4v1H9V3.5H4V5H1zM3 6h7l1.5 5h-10z"/></svg>918-555-3172 (Office)</li>
        <li><svg class="contact-icon" viewBox="0 0 13 12"><path d="M4 0h5a1 1 0 0 1 1 1v10a1 1 0 0 1-1 1H4a1 1 0 0 1-1-1V1a1 1 0 0 1 1-1zm.5 1.5v7.5h4V1.5z"/></svg>918-555-6094</li>
        <li><svg class="contact-icon" viewBox="0 0 13 12"><path d="M3 0h7v4H3zM0 5h13v5h-3v2H3v-2H0zm4 3v3h5V8z"/></svg>918-555-4418</li>
        <li><svg class="contact-icon" viewBox="0 0 13 12"><path d="M0 1.5h13v9H0zm1.2 1.2L6.5 7l5.3-4.3v-.2H1.2z"/></svg>dalewr@plainsmail.net</li>
      </ul>
    </div>
  </section>

  <section class="card card--back">
    <div class="green-panel"></div>
    <div class="tree-art" role="img" aria-label="Company illustration: young tree with balled roots and a small shrub"></div>
    <p class="company">Willow Ridge Nursery</p>
    <div class="details">
      <p class="details__name">Dale Whitford</p>
      <p class="details__role">Owner</p>
      <p class="details__address">48217 W. 150 Road, Grove,<br>OK 74592</p>
      <ul class="contact-list">
        <li>918-555-3172 (Office)<svg class="contact-icon" viewBox="0 0 13 12"><path d="M1 4c0-2 2-3 5.5-3S12 2 12 4v1H9V3.5H4V5H1zM3 6h7l1.5 5h-10z"/></svg></li>
        <li>918-555-6094<svg class="contact-icon" viewBox="0 0 13 12"><path d="M4 0h5a1 1 0 0 1 1 1v10a1 1 0 0 1-1 1H4a1 1 0 0 1-1-1V1a1 1 0 0 1 1-1zm.5 1.5v7.5h4V1.5z"/></svg></li>
        <li>918-555-4418<svg class="contact-icon" viewBox="0 0 13 12"><path d="M3 0h7v4H3zM0 5h13v5h-3v2H3v-2H0zm4 3v3h5V8z"/></svg></li>
        <li>dalewr@plainsmail.net<svg class="contact-icon" viewBox="0 0 13 12"><path d="M0 1.5h13v9H0zm1.2 1.2L6.5 7l5.3-4.3v-.2H1.2z"/></svg></li>
      </ul>
    </div>
  </section>
</body>
</html>
```